Business Card design for new private practice opening

I need a business card design for my new private practice with my new logo uploaded as a file
On the front the logo
On the back: maybe a small logo somewhere?
Priv. Doz. DDr. Corinna Vestaluk
Fachärztin für Allgemein- & Viszeralchirurgie
Address: xxx
Tel: xxx
Mobil:xxx
Webseite:xxx
Email:xxx

Contact Information for Business Card

See project description above for details

Requirements
Nice to have
• I would like the colors of the logo incorporated into the business card

```html
<!DOCTYPE html>
<html lang="de">
<head>
<meta charset="utf-8">
<title>Vestaluk Chirurgie – Visitenkarte</title>
<link rel="stylesheet" href="https://fonts.googleapis.com/css2?family=Lato:wght@400;700;900&display=swap">
<style>
  :root {
    --teal: #46b8b6;
    --grey: #7d7d7f;
    --grey-text: #707072;
    --white: #ffffff;
    --backdrop: #e9e7e4;
  }
  * { box-sizing: border-box; margin: 0; padding: 0; }
  html, body { width: 1200px; height: 977px; overflow: hidden; }
  body {
    background: var(--backdrop);
    font-family: "Lato", Arial, sans-serif;
    display: flex; flex-direction: column; align-items: center; justify-content: center;
    gap: 44px;
  }
  .card {
    position: relative;
    width: 560px; height: 362px;
    background: var(--white);
    border-radius: 22px;
    overflow: hidden;
    box-shadow: 0 6px 18px rgba(0,0,0,.12);
  }
  /* front */
  .card-front { display: flex; align-items: center; justify-content: center; gap: 26px; }
  .brand-dot {
    width: 92px; height: 92px; border-radius: 50%;
    border: 5px solid var(--grey);
  }
  .brand-name {
    color: var(--grey); font-weight: 700; font-size: 46px; line-height: 1.02;
    letter-spacing: 1px; text-transform: uppercase;
  }
  /* back */
  .back-art { position: absolute; inset: 0; }
  .details { position: absolute; left: 238px; top: 70px; right: 24px; }
  .holder-name {
    color: var(--teal); font-weight: 900; font-size: 17px; letter-spacing: .2px;
    text-transform: uppercase; white-space: nowrap;
  }
  .holder-role { color: var(--grey-text); font-size: 13px; margin-top: 2px; }
  .rule { width: 40px; height: 2px; background: var(--teal); margin: 14px 0 16px; }
  .contact-list { list-style: none; color: var(--grey-text); font-size: 13px; line-height: 1.5; }
  .contact-list li { display: flex; gap: 10px; align-items: flex-start; }
  .contact-list svg { width: 12px; height: 12px; margin-top: 4px; flex: none; fill: var(--teal); }
  .contact-list .address { margin-bottom: 6px; }
</style>
</head>
<body>

<section class="card card-front" aria-label="Vorderseite">
  <span class="brand-dot"></span>
  <h1 class="brand-name">Vestaluk<br>Chirurgie</h1>
</section>

<section class="card card-back" aria-label="Rückseite">
  <svg class="back-art" viewBox="0 0 560 362" aria-hidden="true">
    <path d="M0 0 H140 C110 170 200 320 340 362 H0 Z" fill="var(--teal)"/>
    <path d="M154 0 C124 170 212 316 352 362" fill="none" stroke="var(--grey)" stroke-width="5"/>
    <circle cx="178" cy="238" r="82" fill="var(--white)"/>
    <circle cx="178" cy="238" r="70" fill="none" stroke="var(--grey)" stroke-width="5"/>
  </svg>

  <div class="details">
    <h2 class="holder-name">Priv. Doz. DDr. Corinna Vestaluk</h2>
    <p class="holder-role">Fachärztin für Allgemein- &amp; Viszeralchirurgie</p>
    <div class="rule"></div>
    <ul class="contact-list">
      <li class="address">
        <svg viewBox="0 0 12 12"><path d="M6 0a4 4 0 0 0-4 4c0 3 4 8 4 8s4-5 4-8a4 4 0 0 0-4-4zm0 5.5A1.5 1.5 0 1 1 6 2.5a1.5 1.5 0 0 1 0 3z"/></svg>
        <span>Street Address Here, City<br>State, Country, ZIP Code 12345</span>
      </li>
      <li>
        <svg viewBox="0 0 12 12"><path d="M2.5 0 4.5 2.5 3.3 4a7 7 0 0 0 4.7 4.7l1.5-1.2L12 9.5 10.5 12C5 12 0 7 0 1.5z"/></svg>
        <span>+12 (0)1 23456-78901</span>
      </li>
      <li>
        <svg viewBox="0 0 12 12"><path d="M3 0h6a1 1 0 0 1 1 1v10a1 1 0 0 1-1 1H3a1 1 0 0 1-1-1V1a1 1 0 0 1 1-1zm0 2v7h6V2z"/></svg>
        <span>+12 (0)1 23456-78901</span>
      </li>
      <li>
        <svg viewBox="0 0 12 12"><path d="M0 2h12v8H0zm1 1 5 4 5-4z"/></svg>
        <span>corinna@vestalukchirurgie.ac.at</span>
      </li>
      <li>
        <svg viewBox="0 0 12 12"><path d="M6 0a6 6 0 1 0 0 12A6 6 0 0 0 6 0zm0 1.2c.8.9 1.3 2.3 1.4 4.2H4.6C4.7 3.5 5.2 2.1 6 1.2zM4.6 6.6h2.8c-.1 1.9-.6 3.3-1.4 4.2-.8-.9-1.3-2.3-1.4-4.2z"/></svg>
        <span>vestalukchirurgie.ac.at</span>
      </li>
    </ul>
  </div>
</section>

</body>
</html>
```